Small consulting business needs a website designed to highlight value and four offerings

My company is a dynamic consulting firm with four Core Offerings: Learning & Evaluation, Program Management, Facilitation & Coaching; Implementation & Transformation. Our mission is to facilitate organizational change and transformation, and to make space for creativity, joy, belonging, and trust. If done successfully, we grow to better understand ourselves, each other, and the work we do together.

I'd like the website to give a feeling of confidence and clarity. I want the colors to match or compliment my logo. I want to have three tabs - Our Clients, Our Services, and Government.

See attached Word document for additional content. My current website is www.BrightHarborGroup.com.

Some websites I'm inspired by:
https://www.quillmeadowworks.com
https://www.verolandpartners.com
https://tqvb.org

Some websites of people/groups in my field that I find uninspiring:
http://denisehollick.com
https://www.marrowfen.org

Target Market(s)

State and local government agencies, health tech, and corporate HR departments

Industry/Entity Type

public health, aging, government, health tech

Coding

Coded - Design and coding required

Number of Pages Required

4 page

Font styles to use
Other font styles liked:
• Calibri and Merriweather

Colors
0054AA
0677BA
7BADD7
CADEEF
E8F1F8
00AB8E
00BBA5
67D7C9
C6EFE9
E9F9F6
FFC000
F8CF3A
FAE287
FDF2CF
FEFAEE
F0912C
F2A743
F7CA91
FBE8D2
FDF5EE

Requirements
Must have
• Attached logo and content, water colors few, and photos.
Nice to have
• Real pictures, which I can provide to the chosen designer
Should not have
• AI generated characters or cartoons.

```html
<!DOCTYPE html>
<html lang="en">
<head>
<meta charset="utf-8">
<title>Bright Harbor Collaborative</title>
<link rel="stylesheet" href="https://fonts.googleapis.com/css2?family=Merriweather:wght@300;400;700;900&family=Open+Sans:wght@400;600;700&display=swap">
<style>
:root{
  --teal-dark:#00AB8E;
  --teal:#00BBA5;
  --teal-light:#67D7C9;
  --teal-pale:#C6EFE9;
  --teal-mist:#E9F9F6;
  --gold:#FFC000;
  --gold-soft:#F8CF3A;
  --gold-light:#FAE287;
  --orange:#F0912C;
  --orange-soft:#F2A743;
  --orange-light:#F7CA91;
  --ink:#1c2326;
  --ink-deep:#0f3d40;
  --white:#ffffff;
}
*{box-sizing:border-box;margin:0;padding:0}
html,body{width:1200px;height:4918px;overflow:hidden}
body{position:relative;background:var(--white);font-family:"Open Sans",sans-serif;color:var(--ink)}
.abs{position:absolute}
.serif{font-family:"Merriweather",serif}

/* washes */
.wash{position:absolute;border-radius:50%;filter:blur(40px);pointer-events:none}

/* header */
.brand{left:128px;top:8px;display:flex;align-items:center;gap:14px}
.brand-mark{width:62px;height:62px;border-radius:50%;background:var(--gold-soft)}
.brand-name{font-family:"Merriweather",serif;font-size:21px;line-height:30px;color:var(--ink);font-weight:300}
.nav{display:flex;align-items:center;gap:24px;font-size:13px;font-weight:700;letter-spacing:.2px;color:var(--ink)}
.nav .dot{width:5px;height:5px;border-radius:50%;background:var(--teal)}
.top-nav{left:455px;top:52px}
.contact-btn{left:962px;top:42px;width:141px;height:38px;background:var(--gold);color:var(--white);font-size:13px;font-weight:700;display:flex;align-items:center;justify-content:center;letter-spacing:.3px}

/* hero */
.hero-title{left:0;width:1200px;top:124px;text-align:center;font-family:"Merriweather",serif;font-size:36px;line-height:46px;font-weight:400}
.hero-title b{font-weight:700}
.hero-sub{left:0;width:1200px;top:242px;text-align:center;font-size:15px;line-height:28px}
.pill{height:60px;border-radius:30px;color:var(--white);font-family:"Merriweather",serif;font-weight:700;font-size:19px;display:flex;align-items:center;letter-spacing:.3px}
.pill .ico{width:34px;height:34px;border:2px solid var(--white);border-radius:50%}
.pill-learning{left:97px;top:368px;width:279px;background:var(--orange);justify-content:flex-end;padding-right:22px;gap:16px}
.pill-impl{left:820px;top:368px;width:283px;background:var(--teal);padding-left:18px;gap:12px}
.pill-facil{left:95px;top:679px;width:277px;background:var(--teal-light);justify-content:flex-end;padding-right:20px;gap:16px}
.pill-program{left:823px;top:679px;width:280px;background:var(--gold);padding-left:20px;gap:12px;font-size:17px;line-height:19px}
.puzzle{left:382px;top:366px;width:436px;height:420px;border-radius:50%;background:radial-gradient(circle at 40% 40%,#c7c04a 0%,#e7b928 35%,#5f9a82 65%,#1f5f5c 100%);border:8px solid var(--ink-deep)}

.arrow{left:585px;width:30px}

/* headings */
.section-title{left:0;width:1200px;text-align:center;font-family:"Merriweather",serif;font-weight:400}
.section-title b{font-weight:700}
.underline{height:5px;border-radius:3px}

/* features */
.illus{border-radius:50%}
.feature-h{font-family:"Merriweather",serif;font-size:34px;font-weight:400}
.feature-h b{font-weight:700}
.feature-p{font-size:16px;line-height:27px}

/* bands */
.band-text{left:0;width:1200px;text-align:center;font-family:"Merriweather",serif;color:var(--white)}

/* footer */
.footer-bg{left:0;top:4570px;width:1200px;height:348px;background:linear-gradient(180deg,#eef8f5,var(--teal-mist))}
.foot-rule{height:2px;background:var(--teal-light)}
.social{width:28px;height:28px;border-radius:50%;background:var(--gold)}
</style>
</head>
<body>

<!-- background washes -->
<div class="wash" style="left:-160px;top:300px;width:360px;height:520px;background:#fdc94b;opacity:.55"></div>
<div class="wash" style="left:1040px;top:80px;width:300px;height:500px;background:var(--teal-pale);opacity:.8"></div>
<div class="wash" style="left:90px;top:1020px;width:520px;height:480px;background:#8fd0d8;opacity:.45"></div>
<div class="wash" style="left:880px;top:1380px;width:420px;height:560px;background:#fbbf6a;opacity:.55"></div>
<div class="wash" style="left:-120px;top:1900px;width:360px;height:480px;background:#fbe2b0;opacity:.7"></div>
<div class="wash" style="left:-150px;top:3020px;width:320px;height:360px;background:#fcc23b;opacity:.6"></div>
<div class="wash" style="left:1040px;top:3000px;width:280px;height:360px;background:var(--teal-pale);opacity:.9"></div>
<div class="wash" style="left:640px;top:3980px;width:560px;height:560px;background:#7fd7cd;opacity:.5"></div>

<!-- header -->
<header>
  <div class="abs brand">
    <div class="brand-mark" aria-hidden="true"></div>
    <div class="brand-name">Bright Harbor<br>&nbsp;&nbsp;Collaborative</div>
  </div>
  <nav class="abs nav top-nav">
    <span>HOME</span><span class="dot"></span>
    <span>OUR CLIENTS</span><span class="dot"></span>
    <span>OUR SERVICES</span><span class="dot"></span>
    <span>GOVERNMENT</span>
  </nav>
  <a class="abs contact-btn">CONTACT US &nbsp;›</a>
</header>

<!-- hero -->
<section class="hero">
  <h1 class="abs hero-title">A Seat at the Table for Collaboration,<br><b>Learning, and Meaningful Change</b></h1>
  <div class="abs underline" style="left:500px;top:221px;width:270px;height:5px;background:var(--teal)"></div>
  <p class="abs hero-sub">Bright Harbor Collaborative is a dynamic consulting firm with four Core Offerings: Learning &amp; Evaluation,<br>Program Management, Facilitation &amp; Coaching; Implementation &amp; Transformation</p>

  <svg class="abs" style="left:0;top:0" width="1200" height="800" aria-hidden="true">
    <g fill="none" stroke="var(--orange)" stroke-width="2">
      <path d="M376 398 L410 398 L440 440"/>
    </g>
    <path d="M820 398 L790 398 L758 440" fill="none" stroke="var(--teal)" stroke-width="2"/>
    <path d="M372 709 L405 709 L440 680" fill="none" stroke="var(--teal-light)" stroke-width="2"/>
    <path d="M823 709 L795 709 L762 680" fill="none" stroke="var(--gold)" stroke-width="2"/>
  </svg>

  <div class="abs pill pill-learning">LEARNING <span class="ico"></span></div>
  <div class="abs pill pill-impl"><span class="ico"></span> IMPLEMENTATION</div>
  <div class="abs pill pill-facil">FACILITATION <span class="ico"></span></div>
  <div class="abs pill pill-program"><span class="ico"></span> PROGRAM<br>MANAGEMENT</div>

  <div class="abs puzzle" role="img" aria-label="Watercolor illustration of four interlocking puzzle pieces inside a ring in gold, olive and teal"></div>

  <svg class="abs arrow" style="top:848px" width="30" height="48" viewBox="0 0 30 48" aria-hidden="true">
    <path d="M15 2 V44 M3 32 L15 44 L27 32" fill="none" stroke="var(--teal)" stroke-width="3" stroke-linecap="round"/>
  </svg>
</section>

<!-- mission / vision / value -->
<section class="pillars">
  <h2 class="abs section-title" style="top:950px;font-size:44px">Here for you <b>and your team</b></h2>
  <div class="abs underline" style="left:620px;top:1014px;width:250px;background:var(--teal)"></div>

  <div class="abs illus" style="left:115px;top:1088px;width:448px;height:390px;background:radial-gradient(circle at 50% 38%,#f0b63a 0%,#e9a238 40%,#7fb7a8 70%,#d7efe8 100%)" role="img" aria-label="Watercolor illustration of a path leading toward a golden sunrise framed by leafy vines"></div>
  <h3 class="abs feature-h" style="left:630px;top:1152px;color:var(--teal)">Our <b style="font-weight:400">Mission</b></h3>
  <p class="abs feature-p" style="left:634px;top:1222px;width:440px">Our mission is to facilitate organizational change and transformation, and to make space for creativity, joy, belonging, and trust. If done successfully, we grow to better understand ourselves, each other, and the work we do together.</p>

  <svg class="abs" style="left:470px;top:1400px" width="240" height="600" aria-hidden="true">
    <path d="M222 0 V30 Q222 90 162 90 H70 Q8 90 8 150" fill="none" stroke="var(--teal)" stroke-width="2"/>
    <path d="M8 420 V450 Q8 505 70 505 H160 Q222 505 222 570" fill="none" stroke="var(--teal)" stroke-width="2"/>
  </svg>

  <h3 class="abs feature-h" style="left:141px;top:1608px;color:var(--orange)">Our <b style="font-weight:400">Vision</b></h3>
  <p class="abs feature-p" style="left:145px;top:1671px;width:430px">Our vision is to be part of a world where organizations and collaborators connect as human beings first. We envision a future where partners and colleagues strive for ongoing growth together.</p>
  <div class="abs illus" style="left:620px;top:1490px;width:390px;height:380px;background:radial-gradient(circle at 48% 50%,#e8c449 0%,#7fa69a 40%,#2d6a78 62%,#f6d89c 85%,#fdf2cf 100%)" role="img" aria-label="Watercolor illustration of overlapping gold and teal circles"></div>

  <div class="abs illus" style="left:143px;top:1946px;width:430px;height:430px;background:radial-gradient(circle,#fff7df 0%,#f7c74a 28%,#e98a2e 50%,#3f8a6a 70%,rgba(255,255,255,0) 72%)" role="img" aria-label="Illustration of a burst of orange, gold and green brush strokes radiating from a bright center"></div>
  <h3 class="abs feature-h" style="left:630px;top:2026px;color:var(--teal)">Our <b style="font-weight:400">Value</b></h3>
  <p class="abs feature-p" style="left:634px;top:2088px;width:450px">We are the tranquility in chaos. The steady partner always at the table with you.<br>We drive meaningful and measurable change, resulting in sustained progress towards key community outcomes and multi-sector initiatives. Our work produces values realignment, critical technical assistance, and develops strategic plans for innovative organizations ready to elevate their work.</p>
</section>

<!-- teal band -->
<section class="help">
  <svg class="abs" style="left:0;top:2440px" width="1200" height="570" aria-hidden="true">
    <defs>
      <linearGradient id="tealFill" x1="0" y1="0" x2="1" y2="0">
        <stop offset="0" stop-color="#1aa9a9"/><stop offset="1" stop-color="#00b797"/>
      </linearGradient>
    </defs>
    <path d="M0 18 Q420 -10 760 20 Q1000 40 1200 80 V130 Q1000 75 760 70 Q420 55 0 70 Z" fill="var(--gold)"/>
    <path d="M0 12 Q420 -12 760 16 Q1010 40 1200 70 V530 Q950 560 640 540 Q300 515 0 425 Z" fill="url(#tealFill)"/>
    <path d="M0 420 Q320 520 660 540 Q960 560 1200 530 V540 Q950 572 640 556 Q300 535 0 450 Z" fill="var(--gold)"/>
  </svg>
  <h2 class="abs band-text" style="top:2540px;font-size:40px;font-weight:400">We Help Your Team...</h2>
  <div class="abs underline" style="left:560px;top:2593px;width:240px;background:var(--gold)"></div>
  <p class="abs band-text" style="top:2642px;font-size:38px;font-weight:400">Turn bold visions into practical results.</p>
  <p class="abs band-text" style="top:2699px;font-size:28px;font-weight:300;opacity:.75">Empower teams to be better together.</p>
  <p class="abs band-text" style="top:2743px;font-size:28px;font-weight:300;opacity:.55">Transform conflict into opportunity.</p>
  <p class="abs band-text" style="top:2787px;font-size:28px;font-weight:300;opacity:.35">Strengthen community-led systems.</p>
  <p class="abs band-text" style="top:2831px;font-size:28px;font-weight:300;opacity:.15">Foster a sense of belonging...</p>
</section>

<!-- common ground -->
<section class="common">
  <h2 class="abs section-title" style="top:3108px;font-size:64px;font-weight:700;color:var(--ink)">...Find common ground.</h2>
  <div class="abs underline" style="left:455px;top:3193px;width:290px;height:6px;background:var(--gold)"></div>
  <svg class="abs arrow" style="left:599px;top:3300px" width="30" height="48" viewBox="0 0 30 48" aria-hidden="true">
    <path d="M15 2 V44 M3 32 L15 44 L27 32" fill="none" stroke="var(--teal)" stroke-width="3" stroke-linecap="round"/>
  </svg>
</section>

<!-- collaborate band -->
<section class="collab">
  <svg class="abs" style="left:0;top:3400px" width="1200" height="530" aria-hidden="true">
    <defs>
      <linearGradient id="goldFill" x1="0" y1="0" x2="1" y2="1">
        <stop offset="0" stop-color="#fbb93a"/><stop offset=".5" stop-color="#fcb637"/><stop offset="1" stop-color="#f9a63c"/>
      </linearGradient>
    </defs>
    <path d="M0 10 Q300 -5 600 25 Q900 55 1200 30 V420 Q900 520 600 520 Q300 520 0 440 Z" fill="url(#goldFill)"/>
  </svg>
  <h2 class="abs band-text" style="top:3486px;font-size:40px;font-weight:400">We <b>Collaborate With</b></h2>
  <div class="abs underline" style="left:555px;top:3537px;width:240px;background:var(--white)"></div>
  <p class="abs band-text" style="top:3580px;font-size:36px;font-weight:400">Large-scale Companies</p>
  <p class="abs band-text" style="top:3632px;font-size:28px;font-weight:300;opacity:.85">National and local nonprofits</p>
  <p class="abs band-text" style="top:3678px;font-size:28px;font-weight:300;opacity:.65">State government agencies</p>
  <p class="abs band-text" style="top:3720px;font-size:28px;font-weight:300;opacity:.45">International Partnerships &amp; Organizations</p>
  <p class="abs band-text" style="top:3765px;font-size:28px;font-weight:300;opacity:.3;color:var(--gold-light)">Foundations</p>
  <p class="abs band-text" style="top:3809px;font-size:28px;font-weight:300;opacity:.35;color:var(--gold)">Tribal Serving Organizations</p>
  <p class="abs band-text" style="top:3853px;font-size:28px;font-weight:300;opacity:.3;color:var(--gold)">Startups in tech</p>
</section>

<!-- why us -->
<section class="why">
  <h2 class="abs serif" style="left:141px;top:4050px;font-size:48px;font-weight:700">Why Us</h2>
  <div class="abs underline" style="left:141px;top:4119px;width:200px;height:4px;background:var(--teal)"></div>
  <p class="abs feature-p" style="left:141px;top:4143px;width:470px">Through our Core Offerings and guided by our founder's traditional and nontraditional methods for engaging and steering a team, we create a sense of belonging, foster transparency, and help to build stronger relationships.</p>
  <p class="abs feature-p" style="left:141px;top:4284px;width:480px">Our approach helps to drive meaningful change so that organizations and initiatives can clear roadblocks and meet collective goals. Our team's proven ability to transform conflict into opportunity will help to advance your organization and the communities you serve.</p>
  <div class="abs illus" style="left:680px;top:4030px;width:436px;height:440px;border:7px solid var(--ink-deep);background:linear-gradient(160deg,#f9c23c 0%,#f3b53a 38%,#5fa37f 55%,#2a9aa8 72%,#e9b873 90%)" role="img" aria-label="Watercolor illustration of a golden sky over flowing teal water and smooth stones in a circle"></div>
</section>

<!-- footer -->
<footer>
  <div class="abs footer-bg"></div>
  <svg class="abs" style="left:0;top:4565px" width="1200" height="70" aria-hidden="true">
    <path d="M0 60 Q260 20 580 5 L0 48 Z" fill="var(--teal-dark)"/>
    <path d="M0 72 Q300 30 580 5 Q300 40 0 82 Z" fill="var(--teal)"/>
  </svg>
  <div class="abs" style="left:572px;top:4606px;width:60px;height:60px;border-radius:50%;background:var(--gold-soft)" aria-hidden="true"></div>
  <div class="abs brand-name" style="left:500px;top:4680px;width:200px;text-align:center;font-size:21px;line-height:30px">Bright Harbor<br>Collaborative</div>
  <div class="abs foot-rule" style="left:145px;top:4694px;width:350px"></div>
  <div class="abs foot-rule" style="left:700px;top:4694px;width:350px"></div>
  <div class="abs foot-rule" style="left:145px;top:4751px;width:350px"></div>
  <div class="abs foot-rule" style="left:700px;top:4751px;width:350px"></div>
  <nav class="abs nav" style="left:270px;top:4715px;font-size:12px">
    <span>HOME</span><span class="dot"></span><span>OUR CLIENTS</span>
  </nav>
  <nav class="abs nav" style="left:748px;top:4715px;font-size:12px">
    <span>OUR SERVICES</span><span class="dot"></span><span>GOVERNMENT</span>
  </nav>
  <p class="abs" style="left:0;width:1200px;top:4787px;text-align:center;font-size:13px">© 2025 Bright Harbor Collaborative. All Right Reserved</p>
  <div class="abs" style="left:535px;top:4834px;display:flex;gap:10px" aria-label="Social links">
    <span class="social"></span><span class="social" style="background:var(--teal)"></span><span class="social" style="background:var(--teal-dark)"></span><span class="social" style="background:var(--teal)"></span>
  </div>
</footer>

</body>
</html>
```